KORBALT

The business want a professional looking business card. We have a scetch we will add but want the extra upgrade, and would like more suggestions for variations of our business cards.

```html
<!DOCTYPE html>
<html lang="en">
<head>
<meta charset="utf-8">
<title>KORBALT Business Card</title>
<link rel="stylesheet" href="https://fonts.googleapis.com/css2?family=Marcellus&family=Manrope:wght@400;500&display=swap">
<style>
  :root {
    --page-bg: #d9d9d7;
    --ink-brown: #6a4d1f;
    --ink-brown-soft: #7a5d2c;
    --gold-light: #ece3c9;
    --gold-mid: #d3bf85;
    --gold-deep: #ad9456;
    --gold-dark: #7b5e2c;
    --card-white: #ffffff;
    --card-white-shade: #e9e9e9;
  }
  * { box-sizing: border-box; margin: 0; padding: 0; }
  html, body { width: 1125px; height: 1200px; overflow: hidden; }
  body {
    background: var(--page-bg);
    position: relative;
    font-family: "Manrope", sans-serif;
  }
  .card {
    position: absolute;
    left: 150px;
    width: 826px;
    height: 471px;
    border-radius: 22px;
    overflow: hidden;
  }
  .card--front {
    top: 98px;
    background: linear-gradient(90deg, var(--gold-mid) 0%, var(--gold-light) 11%, var(--gold-mid) 30%, var(--gold-deep) 58%, var(--gold-dark) 100%);
  }
  .card--back {
    top: 631px;
    background: linear-gradient(180deg, var(--card-white) 40%, var(--card-white-shade) 100%);
  }
  .holder-name {
    position: absolute; left: 134px; top: 80px;
    font-family: "Marcellus", serif;
    font-size: 38px; color: var(--ink-brown);
    letter-spacing: 0.5px;
  }
  .holder-role {
    position: absolute; left: 134px; top: 133px;
    font-size: 31px; color: var(--ink-brown-soft);
  }
  .holder-fullname {
    position: absolute; left: 134px; top: 176px;
    font-size: 19px; color: var(--ink-brown-soft);
  }
  .contact-list {
    position: absolute; left: 134px; top: 278px;
    list-style: none;
  }
  .contact-list li {
    display: flex; align-items: center; gap: 12px;
    height: 42px;
    font-size: 24px; color: var(--ink-brown);
  }
  .contact-list svg { width: 24px; height: 24px; fill: var(--ink-brown); flex: none; }
  .front-brand {
    position: absolute; left: 520px; top: 200px; width: 190px;
    display: flex; flex-direction: column; align-items: center; gap: 14px;
  }
  .front-brand__dot {
    width: 44px; height: 44px; border-radius: 50%;
    background: var(--ink-brown); opacity: 0.55;
  }
  .front-brand__name {
    font-family: "Marcellus", serif;
    font-size: 24px; letter-spacing: 6px; color: var(--ink-brown);
  }
  .back-brand {
    position: absolute; right: 56px; top: 300px;
    font-family: "Marcellus", serif;
    font-size: 64px; letter-spacing: 12px; color: var(--ink-brown);
  }
</style>
</head>
<body>
  <section class="card card--front">
    <h1 class="holder-name">KORBALT VOSSBERG</h1>
    <p class="holder-role">CEO &amp; Founder</p>
    <p class="holder-fullname">Lars Henrik Vossberg</p>
    <ul class="contact-list">
      <li>
        <svg viewBox="0 0 24 24" aria-hidden="true"><path d="M3 9c0-3 4-5 9-5s9 2 9 5v2h-5V9c-1-.6-2.4-1-4-1s-3 .4-4 1v2H3z M6 12h12l2 8H4z M12 14a2.5 2.5 0 1 0 0 5a2.5 2.5 0 0 0 0-5z"/></svg>
        <span>004791234567</span>
      </li>
      <li>
        <svg viewBox="0 0 24 24" aria-hidden="true"><path d="M2 10l10-7 10 7v11H2z M4 11v8.5l6-4.5z M20 11l-6 4 6 4.5z M5 20.5h14l-7-5z"/></svg>
        <span>korbalt.llc@mailbox.com</span>
      </li>
      <li>
        <svg viewBox="0 0 24 24" aria-hidden="true"><path d="M12 2a10 10 0 1 0 0 20a10 10 0 0 0 0-20z M8 6c2 0 3 1 2.5 2.5S8 10 8.5 12s-1 3-2.5 3c-1-2-1.5-6 2-9z M14 13c2 0 3 1 2.5 3S14 19 13 18s-1-5 1-5z"/></svg>
        <span>www.korbalt.llc</span>
      </li>
    </ul>
    <div class="front-brand">
      <span class="front-brand__dot"></span>
      <span class="front-brand__name">KORBALT</span>
    </div>
  </section>

  <section class="card card--back">
    <p class="back-brand">KORBALT</p>
  </section>
</body>
</html>
```